Social Media Application Design - Android and IOS

I am ready to go live with new social media app however I am not comfortable with the current design. It is a not interactive or attractive enough. Please note the splash screen is a green, so preference would be to keep a green theme although I am more than happy to consider other colours that would improve the design.
The attachment has the app screens that need to be redesigned. They may not need massive changes , however keen to go live so looking for inspired designers to support with this project and many others that I have, including ongoing work on this app.
Target Market(s)
Millenials
Industry/Entity Type
Social
Colors
Designer to choose colors to be used in the design.
Requirements
Must have
- Please see attached document for screens that I would like redesigned. It needs to work with Android and IOS. I am looking for the design and not the functionality.
Nice to have
- Highly interactive design. Please see polling functionality of Loomrix.
Should not have
- should not be complicated - simplicity is the key

```html
<!DOCTYPE html>
<html lang="en">
<head>
<meta charset="utf-8">
<title>Poll App Screens</title>
<link rel="stylesheet" href="https://fonts.googleapis.com/css2?family=Poppins:wght@400;500;600&display=swap">
<style>
:root{
  --bg:#f2f2f2;
  --screen:#f7f7f7;
  --white:#ffffff;
  --ink:#1e1e1e;
  --muted:#9a9a9a;
  --line:#ececec;
  --green:#16c17b;
  --green-soft:#5fcf5a;
  --lime:#a9e12a;
  --grad:linear-gradient(90deg,#15c27c,#6ddc6a);
  --chip-off:#f1f1f1;
}
*{box-sizing:border-box;margin:0;padding:0}
html,body{width:1200px;height:1200px;overflow:hidden;background:var(--bg)}
body{font-family:"Poppins",sans-serif;color:var(--ink)}
.board{position:absolute;left:0;top:0;width:1500px;height:1500px;transform:scale(.8);transform-origin:0 0}
.phone{position:absolute;width:252px;background:var(--screen);box-shadow:0 2px 8px rgba(0,0,0,.12);overflow:hidden}
.status{position:absolute;left:0;right:0;top:0;height:16px;display:flex;justify-content:space-between;align-items:center;padding:0 6px;font-size:7.5px;font-weight:500;background:var(--white)}
.topbar{position:absolute;left:0;right:0;top:16px;height:37px;background:var(--white);border-bottom:1px solid var(--line);display:flex;align-items:center;justify-content:center;font-size:12.5px;font-weight:600}
.topbar .back{position:absolute;left:14px;top:12px}
.card{position:absolute;left:11px;right:11px;background:var(--white);border:1px solid var(--line)}
.label{position:absolute;left:11px;font-size:8.5px;font-weight:500}
.seeall{position:absolute;right:8px;font-size:8px;color:var(--muted)}
.chip{position:absolute;height:24px;display:flex;align-items:center;justify-content:center;font-size:8.5px;color:#fff;background:var(--grad)}
.chip.off{background:var(--chip-off);color:#777}
.chip .x{position:absolute;right:-4px;top:-4px;width:9px;height:9px;border-radius:50%;background:#f05050;border:1.5px solid #fff}
.field{position:absolute;background:#f8f8f8;border:1px solid #eee;font-size:8px;color:#aaa;padding:8px 6px}
.btn{position:absolute;left:11px;right:11px;height:31px;background:var(--grad);color:#fff;font-size:10px;display:flex;align-items:center;justify-content:center;letter-spacing:.5px;box-shadow:0 2px 6px rgba(22,193,123,.3)}
.seg{position:absolute;left:12px;width:202px;height:26px;border:1px solid #d8d8d8;border-radius:13px;display:flex;overflow:hidden;font-size:8.5px;color:#999}
.seg span{flex:1;display:flex;align-items:center;justify-content:center;border-right:1px solid #ddd}
.seg span:last-child{border-right:0}
.seg .on{background:var(--grad);color:#fff}
.tile{position:absolute;background:#fff;border:1px solid #eee;box-shadow:0 1px 4px rgba(0,0,0,.06);display:flex;flex-direction:column;align-items:center;justify-content:flex-end;font-size:8.5px;color:#999;padding-bottom:6px}
.radio{position:absolute;left:11px;display:flex;align-items:center;gap:8px;font-size:8.5px}
.radio i{width:13px;height:13px;border-radius:50%;background:#e2e2e2;display:block}
.radio i.on{background:var(--green-soft);box-shadow:inset 0 0 0 3px #b9ecb6}
.menu-head{position:absolute;left:0;right:0;top:0;height:170px;background:linear-gradient(135deg,#14c47c,#b1ea52)}
.menu-head .status{background:transparent;color:#fff}
.avatar{border-radius:50%;background:linear-gradient(135deg,#e8c9a8,#8b6a52)}
.menu-card{position:absolute;left:11px;right:11px;top:145px;height:318px;background:#fff;box-shadow:0 2px 8px rgba(0,0,0,.08)}
.menu-item{position:absolute;left:22px;right:18px;height:40px;border-bottom:1px solid var(--line);display:flex;align-items:center;gap:10px;font-size:10px;font-weight:500}
.badge{margin-left:auto;width:17px;height:17px;border-radius:50%;background:var(--green-soft);color:#fff;font-size:7.5px;display:flex;align-items:center;justify-content:center}
.note{position:absolute;left:8px;right:8px;height:47px;background:#fff;border:1px solid var(--line);display:flex;align-items:flex-start;gap:8px;padding:8px 10px}
.note.new{border-left:3px solid var(--green-soft)}
.note .who{color:var(--green-soft);font-size:10px;font-weight:500}
.note .what{font-size:8.5px;margin-left:4px}
.note .when{font-size:8.5px;color:var(--muted);margin-top:1px}
.post{position:absolute;left:8px;right:8px;background:#fff;border:1px solid var(--line)}
.post .name{position:absolute;left:49px;top:9px;font-size:8.5px;font-weight:600}
.post .time{position:absolute;left:49px;top:25px;font-size:8.5px;color:var(--muted)}
.votes{position:absolute;right:11px;top:10px;width:38px;height:30px;border:1px solid #ddd;text-align:center;font-size:8.5px;color:#666;line-height:1.1;padding-top:4px}
.votes small{display:block;font-size:5px}
.post .q{position:absolute;left:11px;top:49px;font-size:8.5px;font-weight:500}
.opt{position:absolute;top:74px;width:102px;height:99px;display:flex;align-items:center;justify-content:center;color:#fff;font-size:9px}
.opt.a{left:12px;background:var(--green-soft)}
.opt.b{left:120px;background:var(--lime)}
.or{position:absolute;left:104px;top:113px;width:22px;height:22px;border-radius:50%;background:var(--green-soft);border:2px solid #fff;color:#fff;font-size:7.5px;font-weight:600;display:flex;align-items:center;justify-content:center}
.actions{position:absolute;left:14px;right:10px;bottom:6px;display:flex;justify-content:space-between;font-size:8.5px;color:#999}
.pct{font-size:26px;font-weight:500;color:#fff}
.voted{position:absolute;left:5px;bottom:5px;width:90px;height:14px;background:var(--green-soft);color:#fff;font-size:8px;display:flex;align-items:center;padding-left:8px}
.tag{position:absolute;height:22px;display:flex;align-items:center;justify-content:center;font-size:8.5px;background:var(--chip-off);color:#777}
.tag.on{background:var(--grad);color:#fff}
</style>
</head>
<body>
<div class="board">

<section class="phone" style="left:51px;top:140px;height:473px">
  <div class="menu-head">
    <div class="status"><span>Carrier</span><span>9:41 AM</span><span>100%</span></div>
    <svg style="position:absolute;left:15px;top:29px" width="12" height="12" viewBox="0 0 12 12"><path d="M1 1L11 11M11 1L1 11" stroke="#fff" stroke-width="1.4"/></svg>
    <svg style="position:absolute;right:19px;top:27px" width="16" height="16" viewBox="0 0 16 16"><circle cx="8" cy="8" r="5.5" fill="none" stroke="#fff" stroke-width="1.4" stroke-dasharray="2.2 1.2"/><circle cx="8" cy="8" r="2" fill="none" stroke="#fff" stroke-width="1.2"/></svg>
    <div class="avatar" role="img" aria-label="Profile portrait" style="position:absolute;left:97px;top:27px;width:60px;height:60px;border:2px solid #fff"></div>
    <div style="position:absolute;left:0;right:0;top:102px;text-align:center;color:#fff;font-size:10.5px;font-weight:500">Sam Ridley</div>
    <div style="position:absolute;left:0;right:0;top:120px;text-align:center;color:#fff;font-size:8.5px">samridley@mailbox.test</div>
  </div>
  <div class="menu-card">
    <div style="position:absolute;left:67px;top:15px;display:flex;align-items:center;gap:9px;font-size:8.5px">
      <span style="width:25px;height:12px;border-radius:6px;background:var(--green-soft);position:relative;display:block"><i style="position:absolute;right:2px;top:2px;width:8px;height:8px;border-radius:50%;background:#fff;display:block"></i></span>Allow Notification
    </div>
    <div class="menu-item" style="top:41px"><svg width="12" height="12" viewBox="0 0 12 12"><path d="M1.5 6L6 1.8 10.5 6V11H1.5Z" fill="none" stroke="var(--green)" stroke-width="1.2"/></svg>Home</div>
    <div class="menu-item" style="top:81px"><svg width="12" height="12" viewBox="0 0 12 12"><circle cx="6" cy="4" r="2.6" fill="none" stroke="var(--green)" stroke-width="1.2"/><path d="M1.5 11.5C2 8.5 10 8.5 10.5 11.5" fill="none" stroke="var(--green)" stroke-width="1.2"/></svg>My Profile</div>
    <div class="menu-item" style="top:120px"><svg width="12" height="12" viewBox="0 0 12 12"><path d="M1 1.5H11V8H4L1 10.5Z" fill="none" stroke="var(--green)" stroke-width="1.2"/></svg>My Activities</div>
    <div class="menu-item" style="top:160px"><svg width="12" height="12" viewBox="0 0 12 12"><path d="M2.5 9V5.5A3.5 3.5 0 0 1 9.5 5.5V9H1.5H10.5M5 11H7" fill="none" stroke="var(--green)" stroke-width="1.2"/></svg>Notification<span class="badge">2</span></div>
    <div class="menu-item" style="top:199px"><svg width="12" height="12" viewBox="0 0 12 12"><rect x="3" y="1" width="6" height="10" fill="none" stroke="var(--green)" stroke-width="1.2"/></svg>Contact Us</div>
    <div class="menu-item" style="top:239px"><svg width="12" height="12" viewBox="0 0 12 12"><path d="M7 1.5H10.5V10.5H7M1.5 6H7M4 3.5L1.5 6 4 8.5" fill="none" stroke="var(--green)" stroke-width="1.2"/></svg>Logout</div>
  </div>
</section>

<section class="phone" style="left:334px;top:140px;height:515px">
  <div class="status"><span>Carrier</span><span>9:41 AM</span><span>100%</span></div>
  <div class="topbar"><svg class="back" width="12" height="10" viewBox="0 0 12 10"><path d="M11 5H1.5M5 1L1 5 5 9" fill="none" stroke="#222" stroke-width="1.3"/></svg>Post a Questions</div>
  <div class="card" style="top:65px;height:73px">
    <div class="label" style="top:14px">Your question is about</div><div class="seeall" style="top:14px">see all</div>
    <div class="chip" style="left:11px;top:36px;width:71px">Science</div>
    <div class="chip" style="left:93px;top:36px;width:70px">Health</div>
    <div class="chip" style="left:174px;top:36px;width:47px">Gadgets</div>
  </div>
  <div class="card" style="top:154px;height:110px">
    <div class="label" style="top:8px">What is your Questions ?</div>
    <div class="field" style="left:11px;top:28px;width:206px;height:69px">Type text here....</div>
  </div>
  <div class="card" style="top:277px;height:173px">
    <div class="label" style="top:9px">What are the options ?</div>
    <div class="seg" style="top:30px"><span>Images</span><span class="on">Text</span><span>Audio</span></div>
    <div class="field" style="left:11px;top:84px;width:92px;height:69px">Text question 1 ....</div>
    <div class="field" style="left:122px;top:84px;width:91px;height:69px">Text question 2 ....</div>
  </div>
  <div class="btn" style="top:466px">POST</div>
</section>

<section class="phone" style="left:617px;top:140px;height:513px">
  <div class="status"><span>Carrier</span><span>9:41 AM</span><span>100%</span></div>
  <div class="topbar"><svg class="back" width="12" height="10" viewBox="0 0 12 10"><path d="M11 5H1.5M5 1L1 5 5 9" fill="none" stroke="#222" stroke-width="1.3"/></svg>Post a Questions</div>
  <div class="card" style="top:65px;height:73px">
    <div class="label" style="top:14px">Your question is about</div><div class="seeall" style="top:14px">see all</div>
    <div class="chip" style="left:11px;top:36px;width:71px">Science</div>
    <div class="chip" style="left:93px;top:36px;width:70px">Health</div>
    <div class="chip" style="left:174px;top:36px;width:47px">Gadgets</div>
  </div>
  <div class="card" style="top:155px;height:110px">
    <div class="label" style="top:8px">What is your Questions ?</div>
    <div class="field" style="left:11px;top:28px;width:206px;height:69px">Type text here....</div>
  </div>
  <div class="card" style="top:278px;height:172px">
    <div class="label" style="top:9px">What are the options ?</div>
    <div class="seg" style="top:30px;width:213px"><span>Images</span><span>Text</span><span class="on">Audio</span></div>
    <div class="tile" style="left:12px;top:79px;width:89px;height:79px;color:var(--green-soft)">
      <svg style="margin-bottom:6px" width="26" height="38" viewBox="0 0 26 38"><rect x="8" y="1" width="10" height="22" rx="5" fill="none" stroke="var(--green-soft)" stroke-width="2"/><path d="M2 16A11 11 0 0 0 24 16M13 27V36M7 36H19" fill="none" stroke="var(--green-soft)" stroke-width="2"/></svg>13:00</div>
    <div class="tile" style="left:123px;top:79px;width:89px;height:79px">
      <svg style="margin-bottom:6px" width="26" height="38" viewBox="0 0 26 38"><rect x="8" y="1" width="10" height="22" rx="5" fill="none" stroke="#ccc" stroke-width="2"/><path d="M2 16A11 11 0 0 0 24 16M13 27V36M7 36H19" fill="none" stroke="#ccc" stroke-width="2"/></svg>Hold to record</div>
  </div>
  <div class="btn" style="top:466px">POST</div>
</section>

<section class="phone" style="left:900px;top:140px;height:528px">
  <div class="status"><span>Carrier</span><span>9:41 AM</span><span>100%</span></div>
  <div class="topbar"><svg class="back" width="12" height="10" viewBox="0 0 12 10"><path d="M11 5H1.5M5 1L1 5 5 9" fill="none" stroke="#222" stroke-width="1.3"/></svg>Post a Questions</div>
  <div class="card" style="top:65px;height:73px">
    <div class="label" style="top:14px">Your question is about</div><div class="seeall" style="top:14px">see all</div>
    <div class="chip" style="left:11px;top:36px;width:71px">Science</div>
    <div class="chip" style="left:93px;top:36px;width:70px">Health</div>
    <div class="chip" style="left:174px;top:36px;width:47px">Gadgets</div>
  </div>
  <div class="card" style="top:154px;height:110px">
    <div class="label" style="top:8px">What is your Questions ?</div>
    <div class="field" style="left:11px;top:28px;width:206px;height:69px">Type text here....</div>
  </div>
  <div class="card" style="top:277px;height:191px">
    <div class="label" style="top:9px">What are the options ?</div>
    <div class="seg" style="top:30px"><span class="on">Images</span><span>Text</span><span>Audio</span></div>
    <div class="tile" style="left:12px;top:76px;width:89px;height:81px;justify-content:center;padding:0"><svg width="38" height="30" viewBox="0 0 38 30"><path d="M3 7H11L14 2H24L27 7H35V28H3Z" fill="none" stroke="#ccc" stroke-width="2"/><circle cx="19" cy="17" r="6.5" fill="none" stroke="#ccc" stroke-width="2"/></svg></div>
    <div class="tile" style="left:125px;top:76px;width:89px;height:81px;justify-content:center;padding:0"><svg width="38" height="30" viewBox="0 0 38 30"><path d="M3 7H11L14 2H24L27 7H35V28H3Z" fill="none" stroke="#ccc" stroke-width="2"/><circle cx="19" cy="17" r="6.5" fill="none" stroke="#ccc" stroke-width="2"/></svg></div>
    <div style="position:absolute;left:12px;width:89px;top:170px;text-align:center;font-size:8.5px;color:#999">Upload Option 1</div>
    <div style="position:absolute;left:125px;width:89px;top:170px;text-align:center;font-size:8.5px;color:#999">Upload Option 2</div>
  </div>
  <div class="btn" style="top:483px">POST</div>
</section>

<section class="phone" style="left:1185px;top:140px;height:503px">
  <div class="status"><span>Carrier</span><span>9:41 AM</span><span>100%</span></div>
  <div class="topbar"><svg class="back" width="12" height="10" viewBox="0 0 12 10"><path d="M11 5H1.5M5 1L1 5 5 9" fill="none" stroke="#222" stroke-width="1.3"/></svg>ASKR</div>
  <div class="card" style="top:65px;height:66px">
    <div class="label" style="top:14px">Your question is about</div><div class="seeall" style="top:14px">see all</div>
    <div class="chip" style="left:11px;top:36px;width:71px">Science<i class="x"></i></div>
    <div class="chip" style="left:93px;top:36px;width:70px">Health<i class="x"></i></div>
    <div class="chip" style="left:174px;top:36px;width:47px">Gadgets</div>
  </div>
  <div class="card" style="top:147px;height:82px">
    <div class="label" style="top:8px">Questions</div>
    <div class="radio" style="top:29px"><i class="on"></i>My Questions</div>
    <div class="radio" style="top:52px"><i></i>All Questions</div>
  </div>
  <div class="card" style="top:241px;height:74px">
    <div class="label" style="top:8px">Location (Limit Search To)</div>
    <div style="position:absolute;left:12px;right:12px;top:34px;height:3px;background:#e6e6e6"></div>
    <div style="position:absolute;left:75px;width:118px;top:34px;height:3px;background:var(--green-soft)"></div>
    <i style="position:absolute;left:69px;top:29px;width:13px;height:13px;border-radius:50%;background:var(--green-soft);box-shadow:inset 0 0 0 3px #b9ecb6"></i>
    <i style="position:absolute;left:187px;top:29px;width:13px;height:13px;border-radius:50%;background:var(--green-soft);box-shadow:inset 0 0 0 3px #b9ecb6"></i>
    <div class="label" style="top:50px">5km</div>
    <div style="position:absolute;right:11px;top:50px;font-size:8.5px;font-weight:500">65km</div>
  </div>
  <div class="card" style="top:328px;height:106px">
    <div class="label" style="top:8px">Sort By</div>
    <div class="radio" style="top:29px"><i class="on"></i>Newest</div>
    <div class="radio" style="top:53px"><i></i>Popular</div>
    <div class="radio" style="top:77px"><i></i>Trending</div>
  </div>
  <div class="btn" style="top:447px">APPLY</div>
</section>

<section class="phone" style="left:51px;top:829px;height:463px">
  <div class="status"><span>Carrier</span><span>9:41 AM</span><span>100%</span></div>
  <div class="topbar"><svg class="back" width="12" height="10" viewBox="0 0 12 10"><path d="M11 5H1.5M5 1L1 5 5 9" fill="none" stroke="#222" stroke-width="1.3"/></svg>Post a Questions
    <span style="position:absolute;right:12px;top:8px;width:44px;height:18px;background:var(--grad);color:#fff;font-size:8.5px;font-weight:400;display:flex;align-items:center;justify-content:center">next</span></div>
  <div class="card" style="top:62px;height:31px">
    <svg style="position:absolute;left:10px;top:9px" width="11" height="11" viewBox="0 0 11 11"><circle cx="4.5" cy="4.5" r="3.6" fill="none" stroke="#888" stroke-width="1.1"/><path d="M7.2 7.2L10.5 10.5" stroke="#888" stroke-width="1.1"/></svg>
    <div style="position:absolute;left:0;right:0;top:9px;text-align:center;font-size:8.5px;color:#999">Search topic/interest</div>
    <i style="position:absolute;right:16px;top:10px;width:11px;height:11px;border-radius:50%;background:#bbb"></i>
  </div>
  <div class="card" style="top:103px;height:346px">
    <div style="position:absolute;left:0;right:0;top:13px;text-align:center;font-size:8.5px;font-weight:500">What is your question about?</div>
    <div class="tag on" style="left:13px;top:43px;width:67px">Science</div>
    <div class="tag" style="left:84px;top:43px;width:62px">Technology</div>
    <div class="tag" style="left:153px;top:43px;width:61px">Gadget</div>
    <div class="tag" style="left:49px;top:84px;width:63px">Health</div>
    <div class="tag" style="left:118px;top:84px;width:63px">Fashion</div>
    <div class="tag" style="left:14px;top:124px;width:62px">Technology</div>
    <div class="tag on" style="left:83px;top:124px;width:64px">Languages</div>
    <div class="tag" style="left:153px;top:124px;width:61px">Gadget</div>
    <div class="tag" style="left:49px;top:165px;width:63px">Health</div>
    <div class="tag" style="left:118px;top:165px;width:63px">Fashion</div>
  </div>
</section>

<section class="phone" style="left:334px;top:829px;height:463px">
  <div class="status"><span>Carrier</span><span>9:41 AM</span><span>100%</span></div>
  <div class="topbar"><svg class="back" width="12" height="10" viewBox="0 0 12 10"><path d="M11 5H1.5M5 1L1 5 5 9" fill="none" stroke="#222" stroke-width="1.3"/></svg>Contact Us</div>
  <div class="card" style="top:66px;height:165px">
    <div class="label" style="top:12px">Email Addreess</div>
    <div class="field" style="left:11px;top:31px;width:206px;height:22px;padding:5px 6px">Email Addreess</div>
    <div class="label" style="top:63px">Your Message</div>
    <div class="field" style="left:11px;top:83px;width:206px;height:69px">Type text here....</div>
  </div>
  <div class="btn" style="top:244px">SUBMIT</div>
</section>

<section class="phone" style="left:617px;top:829px;height:463px">
  <div class="status"><span>Carrier</span><span>9:41 AM</span><span>100%</span></div>
  <div class="topbar"><svg class="back" width="12" height="10" viewBox="0 0 12 10"><path d="M11 5H1.5M5 1L1 5 5 9" fill="none" stroke="#222" stroke-width="1.3"/></svg>Notification</div>
  <div class="note new" style="top:63px"><div class="avatar" role="img" aria-label="User portrait" style="width:26px;height:26px;flex:none"></div><div><span class="who">Sam Ridley</span><span class="what">Posted new Questions</span><div class="when">3h ago</div></div></div>
  <div class="note new" style="top:118px"><div class="avatar" role="img" aria-label="User portrait" style="width:26px;height:26px;flex:none"></div><div><span class="who">Sam Ridley</span><span class="what">Posted new Questions</span><div class="when">3h ago</div></div></div>
  <div class="note" style="top:173px"><div class="avatar" role="img" aria-label="User portrait" style="width:26px;height:26px;flex:none"></div><div><span class="who">Sam Ridley</span><span class="what">Answered your question</span><div class="when">3h ago</div></div></div>
  <div class="note" style="top:228px"><div class="avatar" role="img" aria-label="User portrait" style="width:26px;height:26px;flex:none"></div><div><span class="who">Sam Ridley</span><span class="what">Answered your question</span><div class="when">3h ago</div></div></div>
  <div class="note" style="top:283px"><div class="avatar" role="img" aria-label="User portrait" style="width:26px;height:26px;flex:none"></div><div><span class="who">Sam Ridley</span><span class="what">Answered your question</span><div class="when">3h ago</div></div></div>
  <div class="note" style="top:338px"><div class="avatar" role="img" aria-label="User portrait" style="width:26px;height:26px;flex:none"></div><div><span class="who">Sam Ridley</span><span class="what">Answered your question</span><div class="when">3h ago</div></div></div>
</section>

<section class="phone" style="left:900px;top:829px;height:503px">
  <div class="status"><span>Carrier</span><span>9:41 AM</span><span>100%</span></div>
  <div class="topbar"><svg class="back" width="12" height="10" viewBox="0 0 12 10"><path d="M11 5H1.5M5 1L1 5 5 9" fill="none" stroke="#222" stroke-width="1.3"/></svg>HOME</div>
  <article class="post" style="top:66px;height:204px">
    <div class="avatar" role="img" aria-label="User portrait" style="position:absolute;left:11px;top:11px;width:27px;height:27px;background:linear-gradient(135deg,#9db4d8,#3b4a6b)"></div>
    <div class="name">Jana Welles</div><div class="time">3h ago</div>
    <div class="votes">15<small>votes</small></div>
    <div class="q">What is your favourite voice?</div>
    <div class="opt a">Yeahhh!</div><div class="opt b">Nope!</div>
    <div class="or">OR</div>
    <div class="actions"><span>&lt; Share</span><span>● Report</span><span>◉ View More</span></div>
  </article>
  <article class="post" style="top:284px;height:205px">
    <div class="avatar" role="img" aria-label="User portrait" style="position:absolute;left:11px;top:11px;width:27px;height:27px;background:linear-gradient(135deg,#9db4d8,#3b4a6b)"></div>
    <div class="name">Jana Welles</div><div class="time">3h ago</div>
    <div class="votes">15<small>votes</small></div>
    <div class="q">What is your favourite singer?</div>
    <div class="opt a" role="img" aria-label="Singer photo, green tinted" style="background:linear-gradient(135deg,#7fbf6e,#4f8d48)"><span class="pct">55%</span><span class="voted">your voted</span></div>
    <div class="opt b" role="img" aria-label="Singer photo, dark tinted" style="background:linear-gradient(135deg,#5e5143,#2c2620)"><span class="pct">45%</span></div>
    <div class="or">OR</div>
    <div class="actions"><span>&lt; Share</span><span>● Report</span><span>◉ View More</span></div>
  </article>
</section>

<section class="phone" style="left:1198px;top:829px;height:503px">
  <div class="status"><span>Carrier</span><span>9:41 AM</span><span>100%</span></div>
  <div class="topbar"><svg class="back" width="12" height="10" viewBox="0 0 12 10"><path d="M11 5H1.5M5 1L1 5 5 9" fill="none" stroke="#222" stroke-width="1.3"/></svg>HOME</div>
  <article class="post" style="top:66px;height:204px">
    <div class="avatar" role="img" aria-label="User portrait" style="position:absolute;left:11px;top:11px;width:27px;height:27px;background:linear-gradient(135deg,#9db4d8,#3b4a6b)"></div>
    <div class="name">Jana Welles</div><div class="time">3h ago</div>
    <div class="votes">15<small>votes</small></div>
    <div class="q">What is your favourite music artist?</div>
    <div class="opt a" role="img" aria-label="Band photo in black and white" style="background:linear-gradient(135deg,#bdbdbd,#3a3a3a)"></div>
    <div class="opt b" role="img" aria-label="Band photo, green tinted" style="background:linear-gradient(135deg,#8dbb5e,#4e7d3a)"></div>
    <div class="or">OR</div>
    <div class="actions"><span>&lt; Share</span><span>● Report</span><span>◉ View More</span></div>
  </article>
  <article class="post" style="top:284px;height:205px">
    <div class="avatar" role="img" aria-label="User portrait" style="position:absolute;left:11px;top:11px;width:27px;height:27px;background:linear-gradient(135deg,#9db4d8,#3b4a6b)"></div>
    <div class="name">Jana Welles</div><div class="time">3h ago</div>
    <div class="votes">15<small>votes</small></div>
    <div class="q">What is your favourite drink?</div>
    <div class="opt a">Fizzo</div><div class="opt b">Colava</div>
    <div class="or">OR</div>
    <div class="actions"><span>&lt; Share</span><span>● Report</span><span>◉ View More</span></div>
  </article>
</section>

</div>
</body>
</html>
```